MAPLE HARVEST CA$H

We need a postcard to promote a referall program that we are offering to everyone that has purchased a vehicle from us in the past 3 years - - -about 500.
The promotion is titled "maple Harvest Cash" and offers the recipient to earn up to $600, to be passed out the week of Tgiving.

We would require 3 coupons per card 100, 200, 300,and our logo and artwork.
I want it to blast out, catch enough attentioin to read
Front artwork and coupons, back description and rules.

Target Market(s)

our car and truck buyers from the past three years.

Requirements
Must have
• The Front of the postcard should have our Logo, the Promotion and three coupons.
Referal #1 - $100
Referal #2 - $200
Refreal #3 - $300
Each should name the promotion and have a spot for the person refering to write their name.

The back will promote the sale,and provide the timing, and rules.
Nice to have
• fits the excitement of the Season

```html
<!DOCTYPE html>
<html lang="en">
<head>
<meta charset="utf-8">
<title>Maple Harvest Cash Postcard</title>
<link href="https://fonts.googleapis.com/css2?family=Lato:wght@400;700;900&family=Open+Sans+Condensed:wght@700&family=Arimo:wght@400;700&display=swap" rel="stylesheet">
<style>
:root{
  --stage:#ececec;
  --ink:#0b0b0c;
  --navy:#0f2340;
  --red:#e41e2f;
  --white:#ffffff;
  --gold-top:#ffd21a;
  --gold-bottom:#f39a00;
  --paper:#ffffff;
}
*{box-sizing:border-box;margin:0;padding:0}
html,body{width:1200px;height:1000px;overflow:hidden}
body{background:var(--stage);position:relative;font-family:"Lato",sans-serif;color:var(--white)}
.gold{background:linear-gradient(180deg,var(--gold-top),var(--gold-bottom));-webkit-background-clip:text;background-clip:text;color:transparent}

/* Front */
.card-front{position:absolute;left:175px;top:92px;width:483px;height:374px;background:var(--ink);overflow:hidden}
.car-photo{position:absolute;left:0;top:105px;width:160px;height:269px;background:radial-gradient(ellipse at 70% 30%,#4a4c50 0%,#202124 45%,#0b0b0c 85%)}
.front-title{position:absolute;left:24px;top:58px;transform:rotate(-8deg);transform-origin:left top;font-weight:900;font-size:42px;line-height:40px;white-space:nowrap}
.front-title span{display:block}
.front-title .line-2{padding-left:92px}
.front-amount{position:absolute;left:208px;top:132px;font-weight:900;font-size:78px;line-height:80px}
.contact-pill{position:absolute;left:200px;top:213px;width:215px}
.contact-pill .phone{background:var(--red);border-radius:9px 9px 0 0;font-weight:700;font-size:16px;text-align:center;height:25px;line-height:25px}
.contact-pill .web{background:var(--navy);border-radius:0 0 9px 9px;font-weight:700;font-size:16px;text-align:center;height:24px;line-height:23px}
.brand{position:absolute;background:var(--navy);border-radius:6px;display:flex;align-items:center;gap:6px;padding:0 7px}
.brand .mark{width:11px;height:11px;background:var(--red);flex:none}
.brand .name{font-weight:900;font-size:14px;line-height:17px;color:var(--white)}
.card-front .brand{left:22px;top:201px;width:98px;height:74px}

.coupons{position:absolute;left:0;top:288px;width:483px;height:72px;background:var(--navy)}
.coupons::before,.coupons::after{content:"";position:absolute;left:0;right:0;border-top:1px dashed #8fa0b8;z-index:0}
.coupons::before{top:4px}.coupons::after{bottom:6px}
.coupon{position:absolute;top:0;height:72px;z-index:1}
.coupon-1{left:18px;width:141px}
.coupon-2{left:165px;width:152px;background:var(--red);padding-left:7px}
.coupon-3{left:325px;width:141px}
.coupon h3{font-weight:700;font-size:15px;line-height:18px;margin:7px 0 4px 6px}
.field{background:var(--white);color:var(--navy);font-family:"Arimo",sans-serif;font-weight:700;font-size:10px;height:14px;line-height:14px;padding-left:4px;margin-bottom:5px;width:141px}
.coupon-2 .field{width:140px}

/* Back */
.card-back{position:absolute;left:478px;top:507px;width:483px;height:372px;background:var(--paper)}
.back-panel{position:absolute;left:0;top:0}
.back-copy{position:absolute;left:24px;top:20px;font-family:"Arimo",sans-serif}
.back-title{font-family:"Lato",sans-serif;font-weight:900;font-size:25px;letter-spacing:0.6px;line-height:28px;margin-bottom:3px;white-space:nowrap}
.lead{font-weight:700;font-size:11px;line-height:12.5px;margin-bottom:6px;width:315px}
.rules{font-size:9.4px;line-height:11.2px;width:212px}
.rules .big{font-size:12px;font-weight:700}
.cta-arrow{position:absolute;left:7px;top:239px}
.cta-text{position:absolute;left:125px;top:244px;white-space:nowrap}
.cta-text .phone{font-weight:700;font-size:19px;line-height:24px}
.cta-text .phone b{font-weight:900;font-size:20px}
.cta-text .tag{font-family:"Open Sans Condensed",sans-serif;font-weight:700;font-size:11px;line-height:14px}
.cta-text .tag b{font-size:13px}
.card-back .brand{left:22px;top:226px;width:96px;height:68px}
</style>
</head>
<body>

<section class="card-front">
  <div class="car-photo" role="img" aria-label="Photo of a dark sedan front in low light"></div>
  <h1 class="front-title gold"><span>MAPLE HARVEST</span><span class="line-2">CA$H</span></h1>
  <div class="front-amount gold">$600</div>
  <div class="contact-pill">
    <div class="phone">Call us @ 555-214-0187</div>
    <div class="web">www.ridgeway123.com</div>
  </div>
  <div class="brand"><span class="mark"></span><span class="name">Ridgeway Auto Sales</span></div>
  <div class="coupons">
    <div class="coupon coupon-1"><h3>Referal #1 - $100</h3><div class="field">FROM:</div><div class="field">TO:</div></div>
    <div class="coupon coupon-2"><h3>Referal #2 - $200</h3><div class="field">FROM:</div><div class="field">TO:</div></div>
    <div class="coupon coupon-3"><h3>Referal #3 - $300</h3><div class="field">FROM:</div><div class="field">TO:</div></div>
  </div>
</section>

<section class="card-back">
  <svg class="back-panel" width="483" height="372" viewBox="0 0 483 372">
    <defs>
      <radialGradient id="panelShade" cx="0.5" cy="0.45" r="0.7">
        <stop offset="0" stop-color="#3a3a3c"/><stop offset="1" stop-color="#1a1a1b"/>
      </radialGradient>
    </defs>
    <polygon points="0,0 345,0 345,119 252,119 252,306 0,306" fill="url(#panelShade)"/>
  </svg>
  <div class="back-copy">
    <h2 class="back-title gold">MAPLE HARVEST CA$H</h2>
    <p class="lead">Can you use $600.00 when the stores open on Harvest weekend? Ridgeway Auto Sales in Cedar Bay wants to add "Cash" to your Holiday budget. It's Easy!</p>
    <p class="rules">Simply refer 3 people that purchase a vehicle between October 20, 2014 and November 20, 2014 and you can pick up too $600.00 the week of November 24, 2014. Here's how it works:<br>
    First Referral..........$100.00<br>
    Second Referral.......$200.00<br>
    Third Referral..........$300.00<br>
    That's <span class="big">$600.00,</span><br>
    and you never have to leave home!<br>
    Need more information?</p>
  </div>
  <svg class="cta-arrow" width="432" height="52" viewBox="0 0 432 52">
    <polygon points="0,0 408,0 430,26 408,52 0,52" fill="#e41e2f"/>
  </svg>
  <div class="cta-text">
    <div class="phone">Call us @ <b>555-214-0187</b></div>
    <div class="tag">Something for Everyone – Everyone Drives at <b>ridgeway123.com</b></div>
  </div>
  <div class="brand"><span class="mark"></span><span class="name">Ridgeway Auto Sales</span></div>
</section>

</body>
</html>
```